Vorlen - Customer Experience Software Company Web Design

*****UPDATE*****
We've been getting a lot of corporate designs through. Unfortunately this is not what we are looking for. We would like our brand to be more approachable and for the look and feel to to be a bit more fun.
Also the best designs we have received so far have followed the "less is more" approach. Im hoping any news designs will take these aspects into account.
*****************

Background:

Vorlen is a Customer Experience Technology company. We equip business and technology teams with the frameworks, tools and services to help them create compelling experiences for their customers.

Our flagship product - Vorlen CX is an open-source customer experience application framework – it enables organisation to build highly differentiated business applications to deliver compelling experiences to your customers.

Vorlen CX is designed for innovators who understand that unlocking opportunity in today’s competitive marketplace is driven by delivering a better customer experience.

Task:

We are looking for a web design (we need PSD, no HTML/CSS) for our company site through which to launch our customer experience framework product. The site will be also used as a support site, so the functional aspect of the site is as important as the visual impact for sales.

In order to help us conceptualise ideas and content we have drafted a temporary website using a standard wordpress theme (please see details below). Now we have a general idea of our requirements we like we would like to take it to the next level and get some designs with that professional edge.

Our target market are Enterprise organisations - that is senior members of the business & technology teams (Business General Managers, CTO’s, CIO’s, and Senior Architects and Senior Developers). We want something clean & fresh which is DIFFERENT from the typical corporate technology websites out there. We would like to be seen as more approachable than most large technology companies.

Words we would like to use to describe the finished design:
• Clean (we’re thinking white background with one or two key colours)
• Fresh
• Light
• Modern
• Less is more
• Web 2.0
• Fun but professional (aimed at Enterprise/Large organisations)
• Bold, clear call to action – e.g. Live Demo & Download
• Readable (but Sans Serif)

As we’re a Customer Experience company, the usability of the site is critical. The site must be functional, intuitive & easy to navigate. We want to keep the number of user clicks to the bare minimum possible.

Other aspects, which we would like to incorporate into the site
• Home Page banner slider
• Client logon
• Newsletter sign up
• Social media links – Tallyface, Workweave (for starters)
• Rich footer links

Some websites we like
• http://brightpanelworks.example - clean, light, modern & intuitive
• http://www.tamsoledrik.example - bold, clear messaging
• http://www.opengridhub.example/markup/emblem - punchy, colourful
• http://postwren.example/ - modern, clear messaging, colourful, rich footer area

Target Market(s)

Enterprise organisations - that is senior members of the business & technology teams (Business General Managers, CTO’s, CIO’s, Senior Devs)

Industry/Entity Type

Business

Requirements
Must have
• - Design Specs: Accepted file formats: During the design phase adobe PSD or JPEG are OK (if you need to upload files), but for the handover we'll need PSD only with all the original layers.
- The width needs to be a size that will work with every size computer screen
- Need to use cross-platform compatible font
- The graphic elements used for the design must be copyright free

Current test site
- URL http://vorlen.example/wp-admin
- username: artmarket
- password: artmarket

IMPORTANT NOTE REGARDING OUR CURRENT TEST SITE:

This is a very basic version of a site to help us generate requirements. This design is only a starting point/input and is not locked in stone i.e. we do not simply want this site simply tweaked around the edges.

We are looking for you to use all of your graphic design skills and experience to create a truly awesome site design!

```html
<!DOCTYPE html>
<html lang="en">
<head>
<meta charset="utf-8">
<title>Vorlen CX – Customer Experience Framework</title>
<link href="https://fonts.googleapis.com/css2?family=Open+Sans:wght@400;600;700&family=Arimo:wght@400;700&display=swap" rel="stylesheet">
<style>
:root{
  --accent:#ee4a2c;
  --accent-dark:#d63b20;
  --ink:#333;
  --ink-soft:#555;
  --grey-btn:#5e5e5e;
  --band:#e6e6e6;
  --page:#f4f4f4;
  --dark:#2e2e2e;
  --footer:#262626;
  --footer-text:#bdbdbd;
  --green:#7cbf2a;
}
*{box-sizing:border-box;margin:0;padding:0}
html,body{width:986px;height:1200px;overflow:hidden}
body{font-family:"Arimo",Arial,sans-serif;color:var(--ink);background:var(--page)}
.page{position:relative;width:986px;height:1200px;overflow:hidden}
.abs{position:absolute}

.hero{position:absolute;left:0;top:0;width:986px;height:410px;
  background:radial-gradient(ellipse at 62% 40%,#ffffff 0%,#f6f6f6 45%,#ececec 100%)}
.logo{left:130px;top:24px;font-family:"Open Sans",sans-serif;font-size:34px;color:var(--accent);line-height:1}
.tagline{left:130px;top:64px;font-size:10.5px;color:var(--ink-soft)}
.nav a{position:absolute;top:62px;font-size:12.6px;color:#666;text-decoration:none}
.hero-title{left:130px;top:128px;font-family:"Open Sans",sans-serif;font-weight:700;font-size:40px;color:#444;line-height:1.2}
.hero-title span{color:var(--accent)}
.hero-copy{left:132px;top:192px;width:360px;font-size:13.5px;line-height:28.3px;color:#333}
.btn{position:absolute;display:block;border-radius:4px;color:#fff;font-family:"Open Sans",sans-serif;font-weight:700;font-size:16px;text-align:center;line-height:36px;height:36px;text-decoration:none}
.btn-demo{left:132px;top:332px;width:123px;background:linear-gradient(#777,#555)}
.btn-download{left:273px;top:332px;width:123px;background:linear-gradient(#f56a4c,var(--accent-dark))}
.dots{display:flex;gap:4px}
.dots i{display:block;width:8px;height:8px;border-radius:50%;background:#888;border:1px solid #aaa}
.dots i.on{background:var(--green)}

.band{position:absolute;left:0;top:410px;width:986px;height:156px;background:var(--band);border-bottom:1px solid #ccc}
.perk h3{position:absolute;font-family:"Open Sans",sans-serif;font-weight:400;font-size:13.5px;color:#333}
.perk p{position:absolute;width:165px;font-size:11.2px;line-height:17.3px;color:#555}
.perk .mark{position:absolute;border-radius:6px}

.features-title{left:390px;top:595px;font-family:"Open Sans",sans-serif;font-size:17px;color:#333}
.sub{font-size:11px;color:#555}
.checks li{list-style:none;position:absolute;left:396px;font-size:11px;color:#444;padding-left:22px}
.checks svg{position:absolute;left:0;top:-2px}
.features-copy{left:603px;top:640px;width:275px;font-size:11px;line-height:17.3px;color:#444}

.dark{position:absolute;left:0;top:787px;width:986px;height:193px;background:var(--dark);border-top:1px solid #555;border-bottom:1px solid #555}
.box{position:absolute;border:1px solid #4a4a4a;border-radius:3px;background:#2a2a2a}
.box h2{position:absolute;color:#fff;font-family:"Open Sans",sans-serif}
.field{position:absolute;height:24px;background:#fff;border:1px solid #ccc;border-radius:2px;font-size:11px;color:#333;padding:5px 9px;line-height:14px}
.small-btn{position:absolute;height:25px;border-radius:3px;background:linear-gradient(#f05a3c,var(--accent-dark));color:#fff;font-size:12.5px;text-align:center;line-height:25px}
.dark .note{position:absolute;font-size:11px;color:#ddd}
.signup{position:absolute;left:131px;top:920px;width:372px;height:42px;border-radius:5px;overflow:hidden;background:linear-gradient(#777,#595959)}
.signup .ask{position:absolute;left:31px;top:11px;color:#fff;font-size:16px}
.signup .go{position:absolute;left:212px;top:0;width:160px;height:42px;background:linear-gradient(#f05a3c,var(--accent-dark));clip-path:polygon(0 0,100% 0,100% 100%,0 100%,-1px 100%,0 100%,12% 50%,0 0);}
.signup .go span{position:absolute;left:34px;top:11px;color:#fff;font-size:16px}
.social{position:absolute;top:922px;width:40px;height:40px;border-radius:4px}

.footer{position:absolute;left:0;top:980px;width:986px;height:220px;background:var(--footer)}
.fcol h4{position:absolute;top:989px;color:#fff;font-size:12.6px;font-weight:700}
.links{position:absolute;top:1012px;list-style:none}
.links li{font-size:10.5px;line-height:17.3px;color:var(--footer-text)}
.press h5,.blog h5{position:absolute;font-size:10.5px;color:#fff;font-weight:700}
.press p,.blog p{position:absolute;font-size:9.8px;line-height:12.6px;color:#888}
.day{position:absolute;font-size:20px;color:#666;font-weight:700;text-align:center;width:30px;line-height:1}
.mon{position:absolute;font-size:9.5px;color:#666;width:30px;text-align:center}
.copyright{left:126px;top:1169px;font-size:10px;color:#aaa}
</style>
</head>
<body>
<div class="page">

  <header class="hero">
    <div class="abs logo">Vorlen</div>
    <div class="abs tagline">The Customer Experience frame work</div>
    <nav class="nav">
      <a style="left:410px" href="#">Home</a>
      <a style="left:480px" href="#">Products</a>
      <a style="left:569px" href="#">Support</a>
      <a style="left:651px" href="#">Blog</a>
      <a style="left:713px" href="#">About</a>
      <a style="left:797px" href="#">Client login</a>
    </nav>

    <h1 class="abs hero-title"><span>Vorlen</span> CX</h1>
    <p class="abs hero-copy">Vorlen CX is a custamer experiance application framework - it enables you to build highly diffrentiated business applications to deliver compeling experiance to your costumers</p>
    <a class="btn btn-demo" href="#">Live demo</a>
    <a class="btn btn-download" href="#">Download</a>
    <div class="abs dots" style="left:133px;top:392px"><i></i><i></i><i class="on"></i><i></i><i></i></div>

    <svg class="abs" style="left:537px;top:152px" width="333" height="275" viewBox="0 0 333 275">
      <defs>
        <linearGradient id="bezel" x1="0" y1="0" x2="0" y2="1"><stop offset="0" stop-color="#e8e8e8"/><stop offset="1" stop-color="#b9b9b9"/></linearGradient>
        <linearGradient id="stand" x1="0" y1="0" x2="1" y2="0"><stop offset="0" stop-color="#9a9a9a"/><stop offset=".5" stop-color="#e0e0e0"/><stop offset="1" stop-color="#9a9a9a"/></linearGradient>
      </defs>
      <path d="M132 229 h70 l6 36 h-82z" fill="url(#stand)"/>
      <rect x="100" y="264" width="134" height="5" rx="2" fill="#aaa"/>
      <rect x="0" y="0" width="333" height="230" rx="8" fill="url(#bezel)"/>
      <rect x="0" y="0" width="333" height="199" rx="8" fill="#111"/>
      <rect x="0" y="190" width="333" height="9" fill="#111"/>
      <g transform="translate(13 12) scale(0.841)">
        <rect width="368" height="210" fill="#f7f6f6"/>
        <text x="183" y="38" text-anchor="middle" font-family="Arimo,sans-serif" font-weight="700" font-size="15" fill="#333">Vorlen-CX</text>
        <g font-family="Arimo,sans-serif" font-size="6.5" fill="#999">
          <text x="18" y="68">1,500</text><text x="18" y="98">1,000</text><text x="22" y="128">500</text>
          <text x="38" y="166">27 May</text><text x="98" y="166">29 May</text><text x="158" y="166">31 May</text><text x="218" y="166">02 Jun</text><text x="278" y="166">04 Jun</text>
        </g>
        <polygon points="38,112 68,101 98,78 128,91 158,84 188,106 218,113 248,95 278,65 308,101 338,114 338,150 38,150" fill="#d9ecee" opacity=".7"/>
        <polygon points="38,129 68,133 98,129 128,133 158,140 188,139 218,132 248,137 278,144 308,135 338,142 338,152 38,152" fill="#fbe3d8"/>
        <polyline points="38,112 68,101 98,78 128,91 158,84 188,106 218,113 248,95 278,65 308,101 338,114" fill="none" stroke="#8ec8d2" stroke-width="1.5"/>
        <polyline points="38,129 68,133 98,129 128,133 158,140 188,139 218,132 248,137 278,144 308,135 338,142" fill="none" stroke="#f07a55" stroke-width="1.5"/>
        <g fill="#fff" stroke="#8ec8d2" stroke-width="1.5">
          <circle cx="38" cy="112" r="2.5"/><circle cx="68" cy="101" r="2.5"/><circle cx="98" cy="78" r="2.5"/><circle cx="128" cy="91" r="2.5"/><circle cx="158" cy="84" r="2.5"/><circle cx="188" cy="106" r="2.5"/><circle cx="218" cy="113" r="2.5"/><circle cx="248" cy="95" r="2.5"/><circle cx="278" cy="65" r="2.5"/><circle cx="308" cy="101" r="2.5"/><circle cx="338" cy="114" r="2.5"/>
        </g>
        <g fill="#fff" stroke="#f07a55" stroke-width="1.5">
          <circle cx="38" cy="129" r="2.5"/><circle cx="68" cy="133" r="2.5"/><circle cx="98" cy="129" r="2.5"/><circle cx="128" cy="133" r="2.5"/><circle cx="158" cy="140" r="2.5"/><circle cx="188" cy="139" r="2.5"/><circle cx="218" cy="132" r="2.5"/><circle cx="248" cy="137" r="2.5"/><circle cx="278" cy="144" r="2.5"/><circle cx="308" cy="135" r="2.5"/><circle cx="338" cy="142" r="2.5"/>
        </g>
      </g>
    </svg>
  </header>

  <section class="band">
    <div class="perk">
      <h3 style="left:128px;top:22px">Cross platform - Web tablet and Mobile</h3>
      <div class="mark" role="img" aria-label="Markup standard badge" style="left:138px;top:50px;width:56px;height:60px;background:#e5532b"></div>
      <p style="left:211px;top:48px">Lorem Ipsum is simply dummy text of the printing and typeset-ting industry. Lorem Ipsum has been the industry's standard</p>
    </div>
    <div class="perk">
      <h3 style="left:396px;top:22px">Open sourse</h3>
      <div class="mark" role="img" aria-label="Open source licence badge" style="left:400px;top:48px;width:52px;height:52px;border-radius:50%;background:#2a8a3e"></div>
      <p style="left:463px;top:48px">Lorem Ipsum is simply dummy text of the printing and typeset-ting industry. Lorem Ipsum has been the industry's standard</p>
    </div>
    <div class="perk">
      <h3 style="left:642px;top:22px">Plexa webtool kit</h3>
      <div class="mark" role="img" aria-label="Plexa webtool kit badge" style="left:651px;top:54px;width:58px;height:52px;background:#cf2a22"></div>
      <p style="left:722px;top:48px">Lorem Ipsum is simply dummy text of the printing and typeset-ting industry. Lorem Ipsum has been the industry's standard</p>
    </div>
  </section>

  <section class="features">
    <div class="abs" role="img" aria-label="Screenshot of the Vorlen CX application form screen" style="left:128px;top:591px;width:240px;height:156px;border-radius:5px;border:1px solid #c8c8c8;background:linear-gradient(#d8d8d8 0,#d8d8d8 16px,#f9f9f9 16px,#eeeeee 100%)"></div>
    <div class="abs dots" style="left:129px;top:752px;gap:2px"><i style="width:5px;height:5px"></i><i style="width:5px;height:5px"></i><i class="on" style="width:5px;height:5px"></i><i style="width:5px;height:5px"></i><i style="width:5px;height:5px"></i></div>

    <h2 class="abs features-title">The Features</h2>
    <div class="abs sub" style="left:395px;top:618px">Dummy text ever since the 1500</div>
    <ul class="checks">
      <li style="top:644px"><svg width="14" height="12" viewBox="0 0 14 12"><path d="M1 6.5l4 4L13 1.5" fill="none" stroke="#6cbf2a" stroke-width="3"/></svg>Lorem Ipsum is simply</li>
      <li style="top:672px"><svg width="14" height="12" viewBox="0 0 14 12"><path d="M1 6.5l4 4L13 1.5" fill="none" stroke="#6cbf2a" stroke-width="3"/></svg>Typesetting industry.</li>
      <li style="top:699px"><svg width="14" height="12" viewBox="0 0 14 12"><path d="M1 6.5l4 4L13 1.5" fill="none" stroke="#6cbf2a" stroke-width="3"/></svg>Lorem Ipsum has been</li>
      <li style="top:726px"><svg width="14" height="12" viewBox="0 0 14 12"><path d="M1 6.5l4 4L13 1.5" fill="none" stroke="#6cbf2a" stroke-width="3"/></svg>The industry's standard</li>
    </ul>
    <div class="abs sub" style="left:603px;top:618px">Dummy text ever since the 1500</div>
    <p class="abs features-copy">Lorem Ipsum is simply dummy text of the printing and typesetting industry. Lorem Ipsum has been the indus-try's standard dummy text ever since the 1500s, when an unknown printer took a galley of type and scrambl ed it to make a type Lorem Ipsum is simply dummy text of the printing and typesetting industry.</p>
  </section>

  <section class="dark">
    <div class="box" style="left:129px;top:15px;width:374px;height:100px">
      <h2 style="left:18px;top:8px;font-size:20px;font-weight:600">Client login</h2>
      <div class="field" style="left:14px;top:42px;width:131px">user name</div>
      <div class="field" style="left:156px;top:42px;width:131px;letter-spacing:2px">••••••••</div>
      <div class="small-btn" style="left:293px;top:42px;width:74px">Login</div>
      <span class="note" style="left:23px;top:75px">Forget password</span>
      <span class="note" style="left:157px;top:75px"><span style="display:inline-block;width:9px;height:9px;background:#fff;margin-right:6px;vertical-align:-1px"></span>Remember me</span>
    </div>
    <div class="box" style="left:521px;top:15px;width:357px;height:100px">
      <h2 style="left:16px;top:15px;font-size:15px;font-weight:700">Subscribe to Our Newsletter</h2>
      <div class="field" style="left:15px;top:42px;width:227px">email adrress</div>
      <div class="small-btn" style="left:250px;top:42px;width:94px">Subsribe</div>
    </div>
  </section>

  <div class="signup"><span class="ask">Not a member yet ?</span><div class="go"><span>Signup now</span></div></div>
  <a class="social" role="img" aria-label="Tallyface" style="left:523px;background:#3b5b9a"></a>
  <a class="social" role="img" aria-label="Chirplet" style="left:582px;background:#38b6e0"></a>
  <a class="social" role="img" aria-label="Plexa Plus" style="left:641px;background:#333;border:1px solid #555"></a>
  <a class="social" role="img" aria-label="Workweave" style="left:699px;background:#3d63a8"></a>

  <footer class="footer"></footer>
  <div class="fcol">
    <h4 style="left:130px">About Us</h4>
    <ul class="links" style="left:130px"><li>About Vorlen</li><li>Jobs</li><li>Customer Stories</li><li>Press Resources</li><li>Press Releases</li><li>About Vorlen</li><li>Customer Stories</li></ul>
    <h4 style="left:272px">Products</h4>
    <ul class="links" style="left:272px"><li>CMS Platform</li><li>Mobile Applications</li><li>Tablet Apps</li><li>Plexa Toolkit</li><li>CMS Platform</li><li>Mobile Applications</li><li>Plexa Toolkit</li></ul>
    <h4 style="left:385px">Press Room</h4>
    <h4 style="left:605px">Blog Updates</h4>
  </div>
  <div class="press">
    <h5 style="left:386px;top:1014px">December 01</h5>
    <p style="left:386px;top:1031px;width:200px">Lorem Ipsum is simply dummy text of the printing and typesetting industry. Lorem</p>
    <h5 style="left:386px;top:1066px">December 02</h5>
    <p style="left:386px;top:1082px;width:200px">Lorem Ipsum is simply dummy text of the printing and typesetting industry. Lorem</p>
    <h5 style="left:386px;top:1118px">December 03</h5>
    <p style="left:386px;top:1134px;width:200px">Lorem Ipsum is simply dummy text of the</p>
  </div>
  <div class="blog">
    <h5 style="left:605px;top:1014px">Printing and typesetting industry</h5>
    <span class="day" style="left:605px;top:1034px">02</span><span class="mon" style="left:605px;top:1056px">DEC</span>
    <p style="left:642px;top:1031px;width:236px">An unknown printer took a galley of type and scbled it to make a type Lorem Ipsum is simply dummy text An unknown printer took</p>
    <h5 style="left:605px;top:1082px">Printing and typesetting industry</h5>
    <span class="day" style="left:605px;top:1101px">03</span><span class="mon" style="left:605px;top:1124px">DEC</span>
    <p style="left:642px;top:1099px;width:236px">An unknown printer took a galley of type ascmbled it to make a type Lorem Ipsum is siply dummy text of the printing and typesetting industry.</p>
    <p style="left:812px;top:1143px;width:64px;text-align:right;color:#aaa">Visit Blog</p>
  </div>
  <div class="abs copyright">© 2001-2011 All Rights Reserved. Vorlen is a registered trademark</div>

</div>
</body>
</html>
```